Bellucari Wine label**

Hi, we need a design for a white, red and sparkling wine label. We are a small italian restaurant (Bellucari) and we want to release some wines under our personal brand. The restaurant has a rustic, italian provance style with with a slight modern, clean lines look. We would like a design that represent our mission to provide as authentic Italian food as we can, something that feels that it has been brought from the heart of Italy.
https://www.bellucaricafe.example/

```html
<!DOCTYPE html>
<html lang="en">
<head>
<meta charset="utf-8">
<title>Bellucari Wine Labels</title>
<link rel="stylesheet" href="https://fonts.googleapis.com/css2?family=EB+Garamond:wght@400&display=swap">
<style>
  :root {
    --stage-top: #e3e4e9;
    --stage-bottom: #f1f0ec;
    --label-light: #eeeeee;
    --label-dark: #1f1f1f;
    --ink-dark: #2a2a2a;
    --ink-light: #f4f4f4;
    --magenta: #c0196e;
    --plum: #8e2455;
    --yellow: #f2d21b;
    --lime: #b8c92a;
    --teal: #2aa7b0;
    --sky: #7fd0dc;
  }
  * { box-sizing: border-box; margin: 0; padding: 0; }
  html, body { width: 857px; height: 1200px; overflow: hidden; }
  body {
    font-family: "EB Garamond", "Palatino Linotype", serif;
    display: flex;
    flex-direction: column;
  }
  .stage {
    display: flex;
    align-items: center;
    justify-content: center;
  }
  .stage--pinot { height: 557px; background: var(--stage-top); }
  .stage--sangiovese { height: 643px; background: var(--stage-bottom); }

  .label {
    width: 270px;
    display: flex;
    flex-direction: column;
    box-shadow: 0 6px 18px rgba(0,0,0,0.12);
  }
  .label__pattern {
    height: 270px;
    background:
      radial-gradient(ellipse at 25% 30%, var(--yellow) 0 12%, transparent 30%),
      radial-gradient(ellipse at 70% 60%, var(--teal) 0 10%, transparent 28%),
      radial-gradient(ellipse at 40% 80%, var(--lime) 0 12%, transparent 30%),
      radial-gradient(ellipse at 80% 20%, var(--magenta) 0 14%, transparent 32%),
      linear-gradient(135deg, var(--plum), var(--magenta) 45%, var(--plum));
  }
  .label__panel {
    height: 150px;
    display: flex;
    flex-direction: column;
    align-items: center;
    padding-top: 26px;
  }
  .label--light .label__panel { background: var(--label-light); color: var(--ink-dark); }
  .label--dark .label__panel { background: var(--label-dark); color: var(--ink-light); }
  .label__brand {
    font-size: 30px;
    letter-spacing: 0.32em;
    text-transform: lowercase;
    margin-right: -0.32em;
  }
  .label__variety {
    font-size: 20px;
    margin-top: 12px;
  }
  .label__volume {
    font-size: 9px;
    margin-top: auto;
    margin-bottom: 14px;
    letter-spacing: 0.05em;
  }
  .label__stripes { display: block; width: 100%; height: 10px; }
</style>
</head>
<body>
  <section class="stage stage--pinot">
    <article class="label label--light">
      <div class="label__pattern" role="img" aria-label="Swirling marbled pattern in magenta, plum, yellow, lime and teal"></div>
      <div class="label__panel">
        <p class="label__brand">bellucari</p>
        <p class="label__variety">Pinot Grigio</p>
        <p class="label__volume">750ml</p>
      </div>
      <svg class="label__stripes" viewBox="0 0 270 10" preserveAspectRatio="none" aria-hidden="true">
        <rect x="0" width="270" height="10" fill="#8e2455"/>
        <rect x="10" width="12" height="10" fill="#f2d21b"/>
        <rect x="34" width="8" height="10" fill="#2aa7b0"/>
        <rect x="54" width="14" height="10" fill="#b8c92a"/>
        <rect x="80" width="10" height="10" fill="#c0196e"/>
        <rect x="100" width="12" height="10" fill="#7fd0dc"/>
        <rect x="124" width="8" height="10" fill="#f2d21b"/>
        <rect x="144" width="14" height="10" fill="#2aa7b0"/>
        <rect x="170" width="10" height="10" fill="#b8c92a"/>
        <rect x="192" width="12" height="10" fill="#c0196e"/>
        <rect x="216" width="8" height="10" fill="#f2d21b"/>
        <rect x="236" width="14" height="10" fill="#7fd0dc"/>
        <rect x="258" width="8" height="10" fill="#b8c92a"/>
      </svg>
    </article>
  </section>

  <section class="stage stage--sangiovese">
    <article class="label label--dark">
      <div class="label__pattern" role="img" aria-label="Swirling marbled pattern in magenta, plum, yellow, lime and teal"></div>
      <div class="label__panel">
        <p class="label__brand">bellucari</p>
        <p class="label__variety">Sangiovese</p>
        <p class="label__volume">750ml</p>
      </div>
      <svg class="label__stripes" viewBox="0 0 270 10" preserveAspectRatio="none" aria-hidden="true">
        <rect x="0" width="270" height="10" fill="#8e2455"/>
        <rect x="10" width="12" height="10" fill="#f2d21b"/>
        <rect x="34" width="8" height="10" fill="#2aa7b0"/>
        <rect x="54" width="14" height="10" fill="#b8c92a"/>
        <rect x="80" width="10" height="10" fill="#c0196e"/>
        <rect x="100" width="12" height="10" fill="#7fd0dc"/>
        <rect x="124" width="8" height="10" fill="#f2d21b"/>
        <rect x="144" width="14" height="10" fill="#2aa7b0"/>
        <rect x="170" width="10" height="10" fill="#b8c92a"/>
        <rect x="192" width="12" height="10" fill="#c0196e"/>
        <rect x="216" width="8" height="10" fill="#f2d21b"/>
        <rect x="236" width="14" height="10" fill="#7fd0dc"/>
        <rect x="258" width="8" height="10" fill="#b8c92a"/>
      </svg>
    </article>
  </section>
</body>
</html>
```